New Business Card for Quill Fern Designs

I create and make jewellery and Clothing. But when it comes to business card design I fail completely.

Sketching is my area, drawing, putting things together neatly, not so much.

Here is a little blurb about my company:

Quill Fern Designs is a truly unique customer experience. Work one on one with Owner Brenda Okafor to make your costuming dreams come true.

Not after a costume? Browse through the store for a look at beautiful and unique piece of jewellery. Each piece has been put together by Brenda, by hand. You'll find Steampunk, gothic, lolita and other quirky styles.

Want something else? What abotu a pair of warm kitty paws? A Pair of Kitty ears? A pony tail to wear on your jeans? There are so many options and things to choose! You will want to take it all home.

I have attached the previous business card with my mascot "Wren" As you can see there is a very Wren in Cloudmarsh feel to the overall company, with references to The Tin Cobbler, and the idea that "We are all made here".

Colour's to use would be purple and blue. The winning design would show the unique but professional approach that Quill Fern Designs takes when creating each piece for their customers.

Reason: Wanted to give you a chance to go over feed back that has been sent out. I am committed to paying for the design that I will use. I think another week will help tweak things up.

Nerds, Geeks and Sci-Fi people aged 20 - 34 both Male and Female

Store

• Website address: www.quillferndesigns.com

Yeah, rest is up too you!
• Honestly, if you could make the whole thing look like a Rupert Galloway "Wren in Cloudmarsh" Drawing with the same line working style that would be amazing!

But I won't restrict you! I'd like to see what you can come up with.

```html
<!DOCTYPE html>
<html lang="en">
<head>
<meta charset="utf-8">
<title>Quill Fern Design Business Cards</title>
<link rel="stylesheet" href="https://fonts.googleapis.com/css2?family=Ubuntu:wght@400;500;700&family=Kreon:wght@400&display=swap">
<style>
  :root {
    --page: #e9e9ec;
    --card: #f7f7f8;
    --card-shade: #eeeef1;
    --violet: #4b2fc4;
    --violet-deep: #2e1f8f;
    --blue: #2a5fa8;
    --blue-deep: #1c3f7a;
    --sky: #3b8ed6;
    --plum: #5a2d86;
    --ink: #2b2b2f;
    --black: #111114;
  }
  * { box-sizing: border-box; margin: 0; padding: 0; }
  html, body { width: 1200px; height: 861px; overflow: hidden; }
  body {
    background: var(--page);
    font-family: "Ubuntu", Arial, sans-serif;
    color: var(--ink);
    position: relative;
  }
  .card {
    position: absolute;
    top: 260px;
    width: 540px;
    height: 340px;
    background: linear-gradient(160deg, var(--card) 0%, var(--card-shade) 100%);
    box-shadow: 0 14px 30px rgba(0,0,0,0.18);
    overflow: hidden;
  }
  .card--back { left: 40px; }
  .card--front { left: 620px; }

  .band { position: absolute; left: 0; width: 100%; }
  .band--top { top: 0; height: 44px; }
  .band--bottom { bottom: 0; height: 46px; }

  .mascot {
    position: absolute;
    border-radius: 6px;
    background: linear-gradient(180deg, #2a2a30 0%, #2a2a30 16%, #e59a55 24%, #4a3fd6 48%, #5d8fd0 78%, #d9dce6 100%);
    opacity: 0.9;
  }
  .card--back .mascot { left: 34px; top: 62px; width: 150px; height: 150px; }
  .card--front .mascot { left: 26px; top: 56px; width: 224px; height: 240px; }

  .wordmark {
    display: flex;
    align-items: center;
    gap: 8px;
    font-weight: 500;
    color: var(--violet);
    letter-spacing: 0.12em;
    text-transform: uppercase;
    line-height: 1.1;
  }
  .wordmark__mark { flex: none; background: var(--black); }
  .card--back .wordmark { position: absolute; left: 34px; top: 226px; font-size: 17px; width: 190px; }
  .card--back .wordmark__mark { width: 14px; height: 14px; }

  .front-info {
    position: absolute;
    left: 270px;
    right: 34px;
    top: 56px;
    display: flex;
    flex-direction: column;
    align-items: flex-end;
  }
  .card--front .wordmark { font-size: 24px; align-self: center; }
  .card--front .wordmark__mark { width: 18px; height: 18px; }

  .services {
    align-self: center;
    margin-top: 12px;
    text-align: center;
    white-space: nowrap;
    font-family: "Kreon", Georgia, serif;
    font-size: 10px;
    line-height: 1.35;
    color: var(--ink);
  }
  .owner-name {
    margin-top: 16px;
    font-size: 27px;
    font-weight: 500;
    color: var(--plum);
    white-space: nowrap;
  }
  .contact {
    margin-top: 10px;
    list-style: none;
    font-size: 12.5px;
  }
  .contact li { display: flex; align-items: center; justify-content: flex-end; gap: 6px; height: 26px; white-space: nowrap; }
  .contact svg { width: 20px; height: 20px; flex: none; }

  .blurb {
    position: absolute;
    left: 232px;
    top: 56px;
    width: 290px;
    font-size: 12.4px;
    line-height: 1.22;
  }
  .blurb p + p { margin-top: 12px; }
  .blurb strong { color: var(--violet); font-weight: 700; }
  .blurb .owner { color: var(--sky); font-weight: 700; }
  .blurb .lead { color: var(--plum); font-weight: 700; }
</style>
</head>
<body>

  <section class="card card--back" aria-label="Business card back">
    <svg class="band band--top" viewBox="0 0 540 44" preserveAspectRatio="none" aria-hidden="true">
      <path d="M0 0H540V14C440 18 360 22 250 26C160 30 80 30 0 34Z" fill="var(--violet)"/>
      <path d="M0 34C90 30 170 30 260 26L260 29C170 33 90 34 0 38Z" fill="var(--violet-deep)" opacity="0.6"/>
    </svg>

    <div class="mascot" role="img" aria-label="Mascot illustration: Wren in a top hat, sitting"></div>

    <div class="wordmark">
      <span class="wordmark__mark"></span>
      <span>Quill Fern Design</span>
    </div>

    <div class="blurb">
      <p><strong>QUILL FERN DESIGNS</strong> is a truly unique customer experience. Work one on one with Owner <span class="owner">Brenda Okafor</span> to make your costuming dreams come true.</p>
      <p><span class="lead">Not after a costume?</span> Browse through the store for a look at beautiful and unique piece of jewelery. Each piece has been put together by Brenda, by hand. You'll find Steam-punk, Gothic, Lolita and other Quirky styles.</p>
      <p><span class="lead">Want something else?</span> What about a pair of warm kitty paws? A Pair of Kitty ears? A pony tail to wear on your jeans? There are so many options and things to choose! You will want to take it all home.</p>
    </div>

    <svg class="band band--bottom" viewBox="0 0 540 46" preserveAspectRatio="none" aria-hidden="true">
      <path d="M0 30C140 22 300 14 540 4V46H0Z" fill="var(--blue)"/>
      <path d="M0 38C160 30 320 22 540 14V46H0Z" fill="var(--blue-deep)"/>
    </svg>
  </section>

  <section class="card card--front" aria-label="Business card front">
    <svg class="band band--top" viewBox="0 0 540 44" preserveAspectRatio="none" aria-hidden="true">
      <path d="M0 0H540V16C440 20 360 22 250 26C160 30 80 30 0 32Z" fill="var(--violet)"/>
      <path d="M120 34C220 30 320 26 420 22L420 25C320 29 220 33 120 37Z" fill="var(--violet-deep)" opacity="0.6"/>
    </svg>

    <div class="mascot" role="img" aria-label="Mascot illustration: Wren in a top hat, sitting"></div>

    <div class="front-info">
      <div class="wordmark">
        <span class="wordmark__mark"></span>
        <span>Quill Fern<br>Design</span>
      </div>

      <p class="services">• Steampunk Jewelry • kitty ears • paws •<br>tails • custom costumes • lolita •</p>

      <h1 class="owner-name">Brenda Okafor</h1>

      <ul class="contact">
        <li>hello@quillferndesign.com
          <svg viewBox="0 0 20 20" aria-hidden="true">
            <circle cx="10" cy="10" r="9" fill="none" stroke="var(--plum)" stroke-width="1.6"/>
            <rect x="5" y="6.5" width="10" height="7" fill="none" stroke="var(--plum)" stroke-width="1.3"/>
            <path d="M5 6.5L10 10.5L15 6.5" fill="none" stroke="var(--plum)" stroke-width="1.3"/>
          </svg>
        </li>
        <li>www.quillferndesign.com
          <svg viewBox="0 0 20 20" aria-hidden="true">
            <circle cx="10" cy="10" r="9" fill="none" stroke="var(--plum)" stroke-width="1.6"/>
            <rect x="5" y="5.5" width="10" height="8" fill="none" stroke="var(--plum)" stroke-width="1.3"/>
            <path d="M5 8H15" stroke="var(--plum)" stroke-width="1.3"/>
          </svg>
        </li>
      </ul>
    </div>

    <svg class="band band--bottom" viewBox="0 0 540 46" preserveAspectRatio="none" aria-hidden="true">
      <path d="M0 32C140 24 300 16 540 6V46H0Z" fill="var(--blue)"/>
      <path d="M0 40C160 32 320 24 540 16V46H0Z" fill="var(--blue-deep)"/>
    </svg>
  </section>

</body>
</html>
```